Business card to promote business guidance

I need a card design to give to all my customers advertising a way to build a business exactly like the one they just bought from. I have an online store and will include one with each shipment. It should state the way to financial freedom and working for yourself

Target Market(s)

Young Entrepreneurs that want to start and don't know how

Industry/Entity Type

Business

Contact Information for Business Card

"You just bought from a successful company on Vorpex. I have a unique business model, discovered by me, unlike any other that can make anyone successful. Follow me and message me for exactly the same model. If you ever wanted to work for yourself, I will teach you how. It's not a pipe dream, allow me to guide you out of the box."

Colors
85abd2

Requirements
Must have
• website www.loganmerewick.com
instagram @theloganmerewick

```html
<!DOCTYPE html>
<html lang="en">
<head>
<meta charset="utf-8">
<title>Logan Merewick – Business Card</title>
<link rel="stylesheet" href="https://fonts.googleapis.com/css2?family=Questrial&family=PT+Sans&family=Arimo&display=swap">
<style>
  :root {
    --brand-blue: #6699cc;
    --brand-blue-light: #85abd2;
    --paper: #f3f3f3;
    --paper-white: #ffffff;
    --backdrop: #e4e5e6;
  }
  html, body {
    margin: 0;
    padding: 0;
    width: 1200px;
    height: 1100px;
    overflow: hidden;
    background: var(--backdrop);
  }
  .canvas {
    position: relative;
    width: 1200px;
    height: 1100px;
  }
  .card {
    position: absolute;
    left: 162px;
    width: 875px;
    height: 500px;
    overflow: hidden;
    box-shadow: 0 4px 14px rgba(0,0,0,0.12);
  }
  .card--back { top: 35px; background: var(--paper-white); }
  .card--front { top: 565px; background: var(--paper); }
  .card__waves {
    position: absolute;
    inset: 0;
    width: 100%;
    height: 100%;
  }
  .card__message {
    position: absolute;
    left: 300px;
    top: 150px;
    width: 520px;
    margin: 0;
    font-family: "Questrial", sans-serif;
    font-size: 17px;
    line-height: 1.45;
    font-weight: 700;
    color: var(--brand-blue);
  }
  .contact-list {
    position: absolute;
    left: 292px;
    top: 170px;
    margin: 0;
    padding: 0;
    list-style: none;
  }
  .contact-item {
    display: flex;
    align-items: center;
    height: 56px;
    margin-bottom: 34px;
  }
  .contact-item__icon {
    width: 56px;
    height: 56px;
    margin-right: 24px;
    flex: none;
  }
  .contact-item__text {
    color: var(--brand-blue);
    font-size: 30px;
  }
  .contact-item__text--handle { font-family: "PT Sans", sans-serif; }
  .contact-item__text--web { font-family: "Arimo", sans-serif; letter-spacing: 1.5px; }
</style>
</head>
<body>
<main class="canvas">

  <section class="card card--back" aria-label="Card back">
    <svg class="card__waves" viewBox="0 0 875 500" preserveAspectRatio="none" aria-hidden="true">
      <defs>
        <linearGradient id="back-veil" x1="0" y1="0" x2="1" y2="0">
          <stop offset="0" stop-color="#85abd2" stop-opacity="0.9"/>
          <stop offset="1" stop-color="#85abd2" stop-opacity="0.15"/>
        </linearGradient>
      </defs>
      <path d="M0 0 H330 C250 40 240 120 250 200 C262 300 240 420 200 500 H0 Z" fill="url(#back-veil)"/>
      <path d="M0 0 H250 C190 60 200 150 220 240 C238 330 200 430 150 500 H0 Z" fill="var(--brand-blue-light)"/>
    </svg>
    <p class="card__message">"You just bought from a successful company on Vorpex. I have a unique business model, discovered by me, unlike any other that can make anyone successful. Follow me and message me for exactly the same model. If you ever wanted to work for yourself, I will teach you how. It's not a pipe dream, allow me to guide you out of the box."</p>
  </section>

  <section class="card card--front" aria-label="Card front">
    <svg class="card__waves" viewBox="0 0 875 500" preserveAspectRatio="none" aria-hidden="true">
      <defs>
        <linearGradient id="front-veil" x1="0" y1="0" x2="1" y2="0">
          <stop offset="0" stop-color="#6699cc" stop-opacity="0.85"/>
          <stop offset="1" stop-color="#6699cc" stop-opacity="0.25"/>
        </linearGradient>
      </defs>
      <path d="M0 0 H160 C120 90 110 220 170 330 C230 420 280 460 315 500 H0 Z" fill="url(#front-veil)"/>
      <path d="M0 0 H120 C95 100 105 200 150 280 C195 360 200 430 190 500 H0 Z" fill="var(--brand-blue)"/>
      <path d="M125 0 C100 100 110 210 160 300 C205 380 205 440 190 500" fill="none" stroke="#ffffff" stroke-width="2"/>
    </svg>

    <ul class="contact-list">
      <li class="contact-item">
        <svg class="contact-item__icon" viewBox="0 0 56 56" aria-hidden="true">
          <rect x="0" y="0" width="56" height="56" rx="5" fill="var(--brand-blue)"/>
        </svg>
        <span class="contact-item__text contact-item__text--handle">@theloganmerewick</span>
      </li>
      <li class="contact-item">
        <svg class="contact-item__icon" viewBox="0 0 56 56" aria-hidden="true">
          <circle cx="28" cy="28" r="28" fill="var(--brand-blue)"/>
          <g fill="none" stroke="#ffffff" stroke-width="2">
            <circle cx="28" cy="28" r="14"/>
            <ellipse cx="28" cy="28" rx="6" ry="14"/>
            <line x1="14" y1="28" x2="42" y2="28"/>
            <line x1="17" y1="21" x2="39" y2="21"/>
            <line x1="17" y1="35" x2="39" y2="35"/>
          </g>
        </svg>
        <span class="contact-item__text contact-item__text--web">companywebsite.com</span>
      </li>
    </ul>
  </section>

</main>
</body>
</html>
```